harborline slab pumping "just pump it"

I want very easy to understand cards that say everything we offer.
i want the company name/logo, phone number and email on the front of card.
i want the card to stand out, it can be red with black lettering.
on the back of the card i want it to list everything that we can do like a list
the motto is JUST PUMP IT.
the can be in the lower right corner of the back of the card

Target Market(s)

concrete contractors

Industry/Entity Type

Concrete

Contact Information for Business Card

back of the card
Owner:Marco Tellin
Phone:503)418-6093
Email: HSPumping@slabmail.example
address: 22816 se brindle ave Portland, OR 97236

Colors
ec1f27
000000
959595
5c5c5c
f04a50
ffffff
f37122

Requirements
Must have
• :we have years of experience in the world of concrete
• :our pumps can do up to 70 yards an hour
• :if you refer us to other contractors, will give you up to 10% off next pump job
• :don’t hesitate to call if you have any concrete related questions and to get a qoute
• Please put this on the front of the card, “just pump it” in the lower right corner

```html
<!DOCTYPE html>
<html lang="en">
<head>
<meta charset="utf-8">
<title>Harborline Slab Pumping – Business Cards</title>
<link rel="stylesheet" href="https://fonts.googleapis.com/css2?family=Work+Sans:wght@400;500;700&display=swap">
<style>
  :root {
    --brand-red: #ec1f27;
    --card-black: #1e1e1e;
    --card-black-light: #2a2a2a;
    --stage: #161616;
    --white: #ffffff;
    --soft-white: #e6e6e6;
    --rule: #e6e6e6;
  }
  * { box-sizing: border-box; margin: 0; padding: 0; }
  html, body {
    width: 1200px;
    height: 900px;
    overflow: hidden;
    background: var(--stage);
    font-family: "Work Sans", sans-serif;
    color: var(--white);
  }
  .stage {
    position: relative;
    width: 1200px;
    height: 900px;
  }
  .card {
    position: absolute;
    left: 250px;
    width: 700px;
    height: 400px;
    background: linear-gradient(135deg, var(--card-black) 0%, var(--card-black-light) 100%);
    box-shadow: 0 14px 30px rgba(0,0,0,0.55);
  }
  .card--front { top: 40px; }
  .card--back { top: 465px; }

  .brand {
    display: flex;
    align-items: center;
    gap: 14px;
  }
  .brand__dot {
    flex: none;
    border-radius: 50%;
    background: var(--brand-red);
  }
  .brand__name {
    color: var(--brand-red);
    font-weight: 700;
    text-transform: uppercase;
    line-height: 1.05;
  }
  .brand__line { display: block; }

  /* Front */
  .card--front .brand {
    position: absolute;
    left: 50%;
    top: 150px;
    transform: translateX(-50%);
  }
  .card--front .brand__dot { width: 62px; height: 62px; }
  .card--front .brand__name { font-size: 40px; letter-spacing: 2px; }
  .card--front .brand__line--small { font-size: 19px; letter-spacing: 5px; }
  .motto {
    position: absolute;
    right: 44px;
    bottom: 34px;
    font-size: 17px;
    font-weight: 700;
    letter-spacing: 3px;
    text-transform: uppercase;
  }

  /* Back */
  .card--back .brand {
    position: absolute;
    left: 40px;
    top: 92px;
  }
  .card--back .brand__dot { width: 46px; height: 46px; }
  .card--back .brand__name { font-size: 29px; letter-spacing: 1px; }
  .card--back .brand__line--small { font-size: 14px; letter-spacing: 4px; }

  .services {
    position: absolute;
    left: 40px;
    top: 178px;
    width: 310px;
    list-style: none;
  }
  .services__item {
    position: relative;
    padding-left: 16px;
    font-size: 13px;
    line-height: 1.35;
    color: var(--soft-white);
    margin-bottom: 9px;
  }
  .services__item::before {
    content: "";
    position: absolute;
    left: 0;
    top: 6px;
    width: 6px;
    height: 6px;
    background: var(--brand-red);
  }

  .divider {
    position: absolute;
    left: 372px;
    top: 92px;
    width: 2px;
    height: 215px;
    background: var(--rule);
  }
  .contact {
    position: absolute;
    left: 398px;
    top: 92px;
    width: 290px;
  }
  .contact__name {
    color: var(--brand-red);
    font-size: 26px;
    font-weight: 500;
    letter-spacing: 2px;
    text-transform: uppercase;
  }
  .contact__role {
    font-size: 16px;
    margin-bottom: 14px;
  }
  .contact__address {
    font-size: 15px;
    line-height: 1.4;
    margin-bottom: 10px;
  }
  .contact__list { list-style: none; }
  .contact__item {
    display: flex;
    align-items: center;
    gap: 10px;
    font-size: 15px;
    line-height: 1.7;
  }
  .contact__icon { width: 12px; height: 12px; flex: none; }
  .contact__accent { color: var(--brand-red); }
</style>
</head>
<body>
<main class="stage">

  <section class="card card--front" aria-label="Card front">
    <div class="brand">
      <span class="brand__dot"></span>
      <span class="brand__name">
        <span class="brand__line">Harborline</span>
        <span class="brand__line brand__line--small">Slab Pumping</span>
      </span>
    </div>
    <p class="motto">Just pump it.</p>
  </section>

  <section class="card card--back" aria-label="Card back">
    <div class="brand">
      <span class="brand__dot"></span>
      <span class="brand__name">
        <span class="brand__line">Harborline</span>
        <span class="brand__line brand__line--small">Slab Pumping</span>
      </span>
    </div>

    <ul class="services">
      <li class="services__item">Years of experience in the world of concrete</li>
      <li class="services__item">Our pumps do up to 70 yards an hour</li>
      <li class="services__item">Refer us to contractors: up to 10% off your next pump job</li>
      <li class="services__item">Call with any concrete questions or for a quote</li>
    </ul>

    <div class="divider"></div>

    <div class="contact">
      <p class="contact__name">Marco Tellin</p>
      <p class="contact__role">Owner</p>
      <p class="contact__address">22816 SE Brindle Ave<br>Portland, OR 97236</p>
      <ul class="contact__list">
        <li class="contact__item">
          <svg class="contact__icon" viewBox="0 0 12 12" aria-hidden="true"><path d="M2.5 1 L4.5 1 L5.2 3.6 L4 4.6 Q5 7 7.4 8 L8.4 6.8 L11 7.5 L11 9.5 Q10.5 11 9 11 Q1 10 1 2.8 Q1 1.3 2.5 1 Z" fill="#ec1f27"/></svg>
          <span>503)418-6093</span>
        </li>
        <li class="contact__item">
          <svg class="contact__icon" viewBox="0 0 12 12" aria-hidden="true"><rect x="1" y="2.5" width="10" height="7" fill="none" stroke="#ec1f27" stroke-width="1.2"/><path d="M1 2.5 L6 6.5 L11 2.5" fill="none" stroke="#ec1f27" stroke-width="1.2"/></svg>
          <span>HSPumping@slabmail.example</span>
        </li>
        <li class="contact__item">
          <svg class="contact__icon" viewBox="0 0 12 12" aria-hidden="true"><circle cx="6" cy="6" r="5" fill="none" stroke="#ec1f27" stroke-width="1.1"/><ellipse cx="6" cy="6" rx="2.2" ry="5" fill="none" stroke="#ec1f27" stroke-width="1"/><path d="M1 6 H11" stroke="#ec1f27" stroke-width="1"/></svg>
          <span>www.<span class="contact__accent">HSPumping</span>.example</span>
        </li>
      </ul>
    </div>
  </section>

</main>
</body>
</html>
```